Website Design for PawRank - New Digital Agency

We are creating a new digital marketing agency and need a new website. I have attached the logo. Our niche is going to be veterinarians. Use the same colors as in the logo (blue, white and gray).

I want real pictures of real people in this and not just boring stock photos. It needs to be related to the industry.

Home page (example:https://trellmarsh.com/)
Service page (example: https://dovequist.com/consulting/)
Case study page (example: https://www.harlowfinchley.com/seo/case-study/)

I will continue to update this brief.
Updates

I updated the brief with some additional sample sites 2 days ago and want to see more designs. I won't need that may more days ...just a few more.

Target Market(s)

veterinarians

Font styles to use
Sans Serif

Requirements
Must have
• I want a very clean looking site. Use the same colors as in the logo (blue, white and gray).
Nice to have
• We need to build this with the idea that the purpose is to generate leads for our business.
• Home page (example:https://trellmarsh.com/)
• Service page (example: https://dovequist.com/consulting/)
• Case study page (example: https://www.harlowfinchley.com/seo/case-study/)

```html
<!DOCTYPE html>
<html lang="en">
<head>
<meta charset="utf-8">
<title>PawRank – Get More Traffic to your Veterinarian Website</title>
<link href="https://fonts.googleapis.com/css2?family=Montserrat:wght@400;500;600;700&display=swap" rel="stylesheet">
<style>
:root{
  --blue:#0f56a5;
  --blue-bright:#1b5fb4;
  --ink:#333a40;
  --body:#6b7177;
  --muted:#9aa0a6;
  --rule:#d4d4d4;
  --orange:#f6a21b;
  --white:#ffffff;
  --header-bg:#f3f3f3;
}
*{box-sizing:border-box;margin:0;padding:0}
html,body{width:1200px;height:4488px;overflow:hidden}
body{position:relative;background:var(--white);font-family:"Montserrat",Arial,sans-serif;color:var(--body)}
.abs{position:absolute}

/* header */
.site-header{left:0;top:0;width:1200px;height:92px;background:linear-gradient(90deg,#fafafa,var(--header-bg))}
.header-rule{left:84px;top:91px;width:1040px;height:2px;background:var(--rule)}
.brand{left:77px;top:30px;display:flex;align-items:center;gap:8px;font-size:30px;font-weight:700;color:var(--blue);letter-spacing:-.5px}
.brand-dot{width:14px;height:14px;border-radius:50%;background:var(--blue)}
.main-nav{top:38px;font-size:13px;color:var(--ink)}
.main-nav span{position:absolute;white-space:nowrap}
.btn-login{left:984px;top:28px;width:145px;height:40px;border-radius:20px;background:var(--orange);color:#1d1d1d;font-size:13px;font-weight:500;display:flex;align-items:center;justify-content:center}

/* article */
.article-title{left:331px;top:142px;width:560px;font-size:46px;font-weight:400;line-height:56px;color:var(--ink)}
.article-title em{font-style:normal;color:var(--blue-bright)}
.lead{left:331px;top:277px;width:560px;font-size:15.5px;font-weight:700;line-height:30px;color:#22282d;white-space:nowrap}
.lead em{font-style:normal;color:var(--blue-bright)}
.para{left:331px;width:540px;font-size:13.4px;line-height:29px;letter-spacing:.35px;color:var(--body)}
.photo{border-radius:1px}
.photo-desk{left:331px;top:770px;width:537px;height:345px;background:linear-gradient(135deg,#d9d7d2 0%,#7d6b5a 45%,#4a3f36 75%,#b9b9b9 100%)}
.photo-network{left:324px;top:1498px;width:534px;height:401px;background:radial-gradient(ellipse at 50% 40%,#f6d6a8 0%,#e9eef2 40%,#ffffff 75%)}
.photo-vet{left:331px;top:3031px;width:537px;height:357px;background:linear-gradient(90deg,#e7ecef 0%,#7fb5d8 35%,#f2f3f4 65%,#cfd4d8 100%)}

.quote-rule{left:331px;width:99px;height:2px;background:var(--blue-bright)}
.pull-quote{left:331px;top:2342px;width:540px;font-size:30px;line-height:41px;font-weight:400;color:var(--blue-bright)}
.author-avatar{left:331px;top:2531px;width:72px;height:72px;border-radius:50%;background:linear-gradient(160deg,#4d4d4d,#1f1f1f)}
.author-meta{left:420px;top:2547px;font-size:15px;line-height:20px;color:var(--muted);font-weight:500}

.btn-read{left:324px;top:3432px;width:352px;height:51px;border-radius:26px;background:var(--blue);color:var(--white);font-size:15px;font-weight:600;display:flex;align-items:center;justify-content:center;box-shadow:0 14px 30px rgba(15,86,165,.28)}

/* subscribe band */
.cta-band{left:0;top:3597px;width:1200px;height:891px;background:var(--blue)}
.cta-photo{left:0;top:3597px}
.cta-title{left:662px;top:3700px;width:520px;font-size:38px;font-weight:700;line-height:51px;color:var(--white);white-space:nowrap}
.cta-sub{left:666px;top:3891px;width:440px;font-size:13.5px;line-height:22px;color:#d6e2f1}
.email-field{left:648px;top:3972px;width:372px;height:58px;border-radius:29px;background:var(--white);font-size:13px;color:#444;display:flex;align-items:center;padding-left:32px}
.btn-signup{left:939px;top:3978px;width:148px;height:46px;border-radius:23px;background:var(--orange);color:#1d1d1d;font-size:13px;font-weight:600;display:flex;align-items:center;justify-content:center}

.footer-col{top:4207px;font-size:12px;color:#cfdcec}
.footer-col h4{font-size:13.5px;font-weight:700;color:#dfe8f4;margin-bottom:14px}
.footer-col li{list-style:none;line-height:25px}
.social{top:4423px;width:14px;height:14px;border-radius:50%;background:#c7d6ea}
</style>
</head>
<body>

<header>
  <div class="abs site-header"></div>
  <div class="abs header-rule"></div>
  <div class="abs brand"><span class="brand-dot"></span>PawRank</div>
  <nav class="abs main-nav">
    <span style="left:648px">Home</span>
    <span style="left:709px">About</span>
    <span style="left:772px">Tools</span>
    <span style="left:827px">Newsletter</span>
    <span style="left:920px">Contact</span>
  </nav>
  <div class="abs btn-login">Sign up/Login</div>
</header>

<main>
  <h1 class="abs article-title">Get <em>More Traffic</em> to your Veterinarian Website</h1>
  <p class="abs lead">Prima cetero <em>intellegebat id eum, ius iriure impetus no</em>, enim<br>nominati suscipiantur cu pro. Eum an elit lorem ipsum elit<br>aliquid adipisci praesent, id pro laoreet feugait incorrupte.</p>

  <p class="abs para" style="top:398px">Lorem ipsum dolor sit amet, ea pro brute facer propriae, nec epicurei senserit pericula cu. Ea graece animal equidem cum. Ei graece omittantur vel. Habeo persius scaevola qui te. Duo eu mucius nostrum. Causae docendi temporibus vel at. Usu ad postea fabellas, qui nostro iracundia ei. Te vis dicat ludus, an per tale detraxit. Quis vulputate ea pri, essent noluisse sea ex, te nam enim falli. Inciderint temporibus ne cum</p>
  <p class="abs para" style="top:600px">Prima cetero intellegebat id eum, ius iriure impetus no, enim nominati suscipiantur cu pro. Eum an aliquid adipisci praesent, id pro laoreet feugait incorrupte. Ex sed probo nihil quidam. Meliore docendi mandamus ius no. Quo eirmod nostrum intellegebat ad, id duo accusamus</p>

  <div class="abs photo photo-desk" role="img" aria-label="Photo: two people at a wooden café table working on a phone, laptop and tablet"></div>

  <p class="abs para" style="top:1176px">Id quo munere delenit accusamus, his id probatus eleifend, ei fugit simul sed. Cu maiorum suscipiantur sit. Te vis dicat ludus, an per tale detraxit. Quis vulputate ea pri, essent noluisse sea ex, te nam enim falli. Inciderint temporibus ne cum.</p>
  <p class="abs para" style="top:1321px">Lorem ipsum dolor sit amet, ea pro brute facer propriae, nec epicurei senserit pericula cu. Ea graece animal equidem cum. Ei graece omittantur vel. Habeo persius scaevola qui te. Duo eu mucius nostrum. Causae docendi temporibus vel at. Usu ad postea fabellas, qui nostro iracundia ei. Quo eirmod nostrum intellegebat ad, id duo accusamus.</p>

  <div class="abs photo photo-network" role="img" aria-label="Illustration: desktop computer with colourful lines branching into web marketing icons, a desk lamp and a kettle"></div>

  <p class="abs para" style="top:1953px">Lorem ipsum dolor sit amet, ea pro brute facer propriae, nec epicurei senserit pericula cu. Ea graece animal equidem cum. Ei graece omittantur vel. Habeo persius scaevola qui te. Duo eu mucius nostrum. Causae docendi temporibus vel at. Usu ad postea fabellas, qui nostro iracundia ei. Te vis dicat ludus, an per tale detraxit. Quis vulputate ea pri, essent noluisse sea ex, te nam enim falli. Inciderint temporibus ne cum</p>
  <p class="abs para" style="top:2157px">Prima cetero intellegebat id eum, ius iriure impetus no, enim nominati suscipiantur cu pro. Eum an aliquid adipisci praesent, id pro laoreet feugait incorrupte. Ex sed probo nihil quidam. Meliore docendi mandamus ius no. Quo eirmod nostrum intellegebat ad, id duo accusamus</p>

  <div class="abs quote-rule" style="top:2309px"></div>
  <blockquote class="abs pull-quote">Lorem ipsum dolor sit amet, ea pro brute facer propriae, nec epicurei senserit pericula cu. Ea animal elit erat lorem equidem cum.</blockquote>
  <div class="abs author-avatar" role="img" aria-label="Author portrait"></div>
  <div class="abs author-meta">Martin Ellery<br>Author &amp; Marketer</div>
  <div class="abs quote-rule" style="top:2647px"></div>

  <p class="abs para" style="top:2702px">Id quo munere delenit accusamus, his id probatus eleifend, ei fugit simul sed. Cu maiorum suscipiantur sit. Te vis dicat ludus, an per tale detraxit. Quis vulputate ea pri, essent noluisse sea ex, te nam enim falli. Inciderint temporibus ne cum.</p>
  <p class="abs para" style="top:2847px">Lorem ipsum dolor sit amet, ea pro brute facer propriae, nec epicurei senserit pericula cu. Ea graece animal equidem cum. Ei graece omittantur vel. Habeo persius scaevola qui te. Duo eu mucius nostrum. Causae docendi temporibus vel at. Usu ad postea fabellas, qui nostro iracundia ei. Quo eirmod nostrum intellegebat ad, id duo accusamus.</p>

  <div class="abs photo photo-vet" role="img" aria-label="Photo: veterinarian in blue scrubs holding a clipboard beside a dog on an exam table"></div>

  <div class="abs btn-read">Read More about Getting Results</div>
</main>

<section>
  <div class="abs cta-band"></div>
  <svg class="abs cta-photo" width="600" height="891" viewBox="0 0 600 891">
    <defs>
      <linearGradient id="vetShade" x1="0" y1="0" x2="1" y2="1">
        <stop offset="0" stop-color="#e9ecef"/>
        <stop offset=".5" stop-color="#8fb3d6"/>
        <stop offset="1" stop-color="#eef0f2"/>
      </linearGradient>
    </defs>
    <polygon role="img" aria-label="Photo: veterinarian with a stethoscope examining a dog" points="0,0 600,0 360,620 0,620" fill="url(#vetShade)"/>
  </svg>
  <h2 class="abs cta-title">Do You Want More<br>Traffic to your<br>Veterinary Website?</h2>
  <p class="abs cta-sub">Enter your email below to get access to my proven SEO and traffic tips</p>
  <div class="abs email-field">Email Address</div>
  <div class="abs btn-signup">Sign Up Now!</div>
</section>

<footer>
  <div class="abs footer-col" style="left:632px"><h4>What We Do</h4><ul><li>Solutions</li><li>Products</li><li>Resources</li><li>Our Customers</li></ul></div>
  <div class="abs footer-col" style="left:775px"><h4>Company</h4><ul><li>About Us</li><li>Our Team</li><li>Careers</li><li>Legal</li><li>Contact</li></ul></div>
  <div class="abs footer-col" style="left:897px"><h4>Support</h4><ul><li>Features</li><li>Pricing</li><li>Team</li><li>Contact</li><li>Login</li></ul></div>
  <div class="abs footer-col" style="left:1000px"><h4>Legal</h4><ul><li>Legal</li><li>Terms Of Service</li><li>Privacy Policy</li></ul></div>
  <div class="abs social" style="left:1024px"></div>
  <div class="abs social" style="left:1055px"></div>
  <div class="abs social" style="left:1086px"></div>
</footer>

</body>
</html>
```